Food van signage

I need a design that will be used for the decoration of a white fibreglass food van that is currently being built. Please see www.trundlecraft.example to see the van.
I have a Poffertjes (mini Dutch pancake) business and will take my van to markets, fetes and events.
I have two Poffertjes images that I purchased from Pixelmarsh Images, that I have attached. You can incorporate these if you want to.
Until now, I have used a very simple design for my signage which I have attached but I am now ready to take my business to the next level. I prefer simple and clear design rather than overly fussy or frilly.
I do like the idea of a vintage or retro feel to the new design, a bit like an American diner sign or cookbook cover etc and a good injection of colour as the van is white.
I have also attached images I found online that were appealing.
The van is 3m long, 1.5m wide and 2m high. There is a servery window on both sides that is 2.2m long and 1m high.
I want to use the same design on both sides and it needs to include the list of toppings to be written either side of the servery windows.
TOPPINGS
Butter (Traditional)
Maple Syrup
Lemon Juice
Strawberry Jam and Cream
Chocolate
All served with Icing Sugar.
I would also like written somewhere "Available for markets, events and fetes" to encourage more business.
I need a design for the back of the van, which has a door. (Sorry I don't have measurements yet) Text to be included, "Like Us? We're easier to follow on Facebook. www.facebook.com/BrokenHarbourBites"
The other end of the van needs a design but no specific wording needed.
I also find it beneficial to add the words "Mini Dutch Pancakes" because some people don't know what Poffertjes are.
Overall, I need the design to be visually effective from a distance, appealing to men and women... and something that makes you want to indulge in a pancake!
This van is a huge purchase for my little weekend business so I want it to be as effective and locally iconic as possible. Thank You.

Dear Designers, I would like to thank you all for your time and submissions.  It has been very difficult to not choose many of them but a new design was submitted in the last hours yesterday which has won the design.  Everyone kept to brief and submitted great designs and made changes but a new design came in that captured the brief as well as giving us a strong logo design that will strengthen our branding long term.  This was not part of the brief and not expected but was too good to pass up.  This was the final reason for our choice.  We are in the process of making final changes to this submission and then we will close the brief.  Thank you all again.

Target Market(s)

appealing to men, women & children. not too masculine or too feminine

Industry/Entity Type

Events

Requirements
Must have
• 1. Retro/vintage/American dinner style
2. Ideally I don't want to have to pay for a full body wrap so if you can do an effective design that is only a part wrap that would be favourable.
Nice to have
• As van is white, an injection of colour would be nice. I don't have a preference of colour but I need the van to stand out in a market full of marquees and other vans.

```html
<!DOCTYPE html>
<html lang="en">
<head>
<meta charset="utf-8">
<title>Food Van Sticker Design – Poffertjes</title>
<link href="https://fonts.googleapis.com/css2?family=Federo&family=Limelight&family=Cabin+Condensed:wght@400;600&family=Open+Sans:wght@400&family=Playfair+Display:ital@1&display=swap" rel="stylesheet">
<style>
  :root{
    --guide:#e8436a;
    --teal:#6fbfc5;
    --teal-dark:#3f9aa1;
    --pink:#f3bdbd;
    --cream:#ece3c4;
    --brown:#3a2a22;
    --tan:#a5825a;
    --board:#3a2a2e;
    --topping-pink:#ee7fa6;
    --red:#c8393f;
    --white:#ffffff;
  }
  *{box-sizing:border-box;margin:0;padding:0}
  html,body{width:1200px;height:1000px;overflow:hidden;background:var(--white)}
  .sheet{position:relative;width:1200px;height:1000px;font-family:"Open Sans",sans-serif}

  .guide-label{position:absolute;color:var(--guide);font-size:16px;font-family:"Open Sans",sans-serif;white-space:nowrap}
  .guides{position:absolute;inset:0}

  .panel{position:absolute;top:190px;height:502px;
    background:linear-gradient(to bottom,var(--white) 0%,var(--white) 30%,var(--cream) 72%,var(--cream) 100%)}
  .panel--end{left:52px;width:376px}
  .panel--side{left:428px;width:752px}

  .stripe-band{position:absolute;left:52px;top:622px;width:1128px;height:70px;
    background:repeating-linear-gradient(to right,var(--teal) 0 36px,var(--cream) 36px 40px,var(--pink) 40px 76px,var(--cream) 76px 80px)}

  .yum-sign{position:absolute;width:116px;height:58px;background:var(--teal);
    color:var(--white);font-family:"Federo",sans-serif;font-size:40px;line-height:58px;text-align:center;
    transform:rotate(-14deg);box-shadow:4px 4px 0 var(--brown)}

  .photo{position:absolute;border-radius:50%}
  .photo--plate{background:radial-gradient(ellipse at 50% 50%,#e2ad5e 0 38%,var(--teal) 39% 70%,transparent 71%)}
  .photo--fork{border-radius:20px;background:linear-gradient(135deg,#dfe4e6 0%,#b9c0c3 30%,#e5b56c 55%,#c98b3b 100%)}

  .slogan{position:absolute;width:220px;font-family:"Federo",sans-serif;color:var(--brown);
    font-size:19px;line-height:28px;text-align:center;letter-spacing:.5px;text-transform:uppercase;white-space:nowrap}
  .slogan span{font-size:24px}

  .toppings-title{position:absolute;left:474px;top:368px;font-family:"Limelight",sans-serif;
    color:var(--red);font-size:22px;letter-spacing:1px;text-transform:uppercase;white-space:nowrap}
  .toppings-board{position:absolute;left:462px;top:404px;width:132px;height:170px;background:var(--board);
    border-radius:10px;border:3px solid var(--white);outline:2px solid var(--teal);transform:rotate(2deg);
    padding:22px 0 0 12px}
  .toppings-board li{list-style:none;font-family:"Cabin Condensed",sans-serif;color:var(--topping-pink);
    font-size:11px;margin-bottom:15px;white-space:nowrap}
  .toppings-board b{font-weight:600}
  .events-ribbon{position:absolute;left:447px;top:597px;width:178px;height:16px;background:var(--board);
    color:var(--topping-pink);font-family:"Playfair Display",serif;font-style:italic;font-size:9px;
    line-height:16px;text-align:center;white-space:nowrap;clip-path:polygon(0 0,100% 0,96% 50%,100% 100%,0 100%,4% 50%)}

  .servery-window{position:absolute;left:612px;top:268px;width:378px;height:245px;
    border:1.5px dashed var(--guide);border-radius:24px}
  .window-tagline{position:absolute;left:662px;top:460px;font-family:"Federo",sans-serif;color:var(--tan);
    font-size:24px;letter-spacing:3px;text-transform:uppercase;white-space:nowrap}

  .brand-name{position:absolute;left:662px;top:522px;font-family:"Federo",sans-serif;color:var(--teal-dark);
    font-size:62px;line-height:66px;white-space:nowrap}
  .brand-sub{position:absolute;left:796px;top:590px;font-family:"Cabin Condensed",sans-serif;color:var(--brown);
    font-size:16px;letter-spacing:.5px;white-space:nowrap}
</style>
</head>
<body>
<div class="sheet">

  <div class="panel panel--end"></div>
  <div class="panel panel--side"></div>
  <div class="stripe-band"></div>

  <svg class="guides" width="1200" height="1000" viewBox="0 0 1200 1000" aria-hidden="true">
    <g stroke="#e8436a" stroke-width="1" fill="none">
      <rect x="52" y="190" width="1128" height="502"/>
      <line x1="428" y1="190" x2="428" y2="720"/>
      <line x1="52" y1="692" x2="52" y2="720"/>
      <line x1="1180" y1="692" x2="1180" y2="720"/>
      <line x1="52" y1="708" x2="1180" y2="708"/>
      <line x1="30" y1="190" x2="52" y2="190"/>
      <line x1="30" y1="690" x2="52" y2="690"/>
      <line x1="40" y1="190" x2="40" y2="690"/>
      <line x1="860" y1="180" x2="858" y2="262"/>
      <path d="M853 256 L858 264 L863 256"/>
    </g>
  </svg>

  <div class="guide-label" style="left:52px;top:156px">Food Van Sticker Design</div>
  <div class="guide-label" style="left:788px;top:156px">Servery Window</div>
  <div class="guide-label" style="left:14px;top:410px;transform:rotate(-90deg);transform-origin:left top">2 Mtrs.</div>
  <div class="guide-label" style="left:206px;top:714px">1.5 Mtrs.</div>
  <div class="guide-label" style="left:778px;top:714px">3 Mtrs.</div>

  <!-- End panel -->
  <div class="yum-sign" style="left:90px;top:290px">YUM!</div>
  <div class="photo photo--plate" role="img" aria-label="Plate of poffertjes with syrup, cream and strawberry" style="left:146px;top:370px;width:180px;height:130px"></div>
  <div class="slogan" style="left:132px;top:526px"><span>W</span>e always<br>serve fast,<br>fresh &amp; <span>F</span>luffy</div>

  <!-- Side panel -->
  <div class="toppings-title">Topping</div>
  <ul class="toppings-board">
    <li><b>Butter</b> (Traditional)</li>
    <li><b>Maple</b> Syrup</li>
    <li><b>Lemon</b> Juice</li>
    <li><b>Strawberry</b> Jam &amp; Cream</li>
    <li><b>Chocolate</b></li>
  </ul>
  <div class="events-ribbon">• Available for markets and fetes. •</div>

  <div class="servery-window"></div>
  <div class="photo photo--fork" role="img" aria-label="Fork lifting a stack of poffertjes" style="left:760px;top:282px;width:180px;height:160px"></div>
  <div class="yum-sign" style="left:670px;top:306px">YUM!</div>
  <div class="window-tagline">Fast, fresh &amp; Fluffy</div>

  <div class="brand-name">Poffertjes</div>
  <div class="brand-sub">Mini Dudh Pancake</div>

  <div class="photo photo--plate" role="img" aria-label="Plate of poffertjes with syrup, cream and strawberry" style="left:1010px;top:400px;width:150px;height:112px"></div>
  <div class="slogan" style="left:970px;top:536px"><span>W</span>e always<br>serve fast,<br>fresh &amp; <span>F</span>luffy</div>

</div>
</body>
</html>
```